依頼詳細
外壁塗装専門店のビル(三階建て)の袖看板のデザインをお願い致します。
創業55年になりますが、社名も変更し、新社屋に移転したこともあり、認知度を上げるため、一目見ただけで外壁塗装業だと分かるデザインが希望です。未来的かつ、温かみのある看板にしたいと思っております。近辺には複数の看板が立っておりますので、目立つデザインを希望します。サイズや表記内容は「記載項目」をご覧ください。
記載項目
会社名:㈱ホシオラント
ロゴ:添付ファイル
サイズ:W1200×H4000
希望イメージ
シンプル 複雑
単色 カラフル
暗い 明るい
日常 高級
遊び心 厳粛
未来的 伝統的
女性的 男性的
希望する色
青系、水色系、黄・オレンジ系
納品ファイル
• 高解像度JPG (.jpg)
補足説明
看板のサイズが間違っていました。
H3600 W900です。

一目見て「外壁塗装」とわかるインパクトのある文字の大きさと色、シンプルかつ温かみのあるイラストに心惹かれました。

この度は沢山のご提案を有難うございました。素敵なデザインばかりで新しい提案があがってくる度、うきうきしながら見させていただいていました。また機会がありましたら宜しくお願い致します。

```html
<!DOCTYPE html>
<html lang="ja">
<head>
<meta charset="utf-8">
<title>㈱ホシオラント様 看板デザイン案</title>
<link rel="stylesheet" href="https://fonts.googleapis.com/css2?family=Noto+Sans+JP:wght@400;700;900&display=swap">
<style>
  :root {
    --page-bg: #f2f2f2;
    --sign-blue: #2f6fc2;
    --sign-blue-deep: #2560ad;
    --white: #ffffff;
    --orange: #f29a1d;
    --green: #5aa83a;
    --maroon: #8e2f2a;
    --ink: #333333;
    --label: #8a8a8a;
    --deco-light: #9cc6ee;
  }
  * { margin: 0; padding: 0; box-sizing: border-box; }
  html, body { width: 848px; height: 1200px; overflow: hidden; }
  body {
    background: var(--page-bg);
    font-family: "Noto Sans JP", sans-serif;
    position: relative;
  }
  .size-label {
    position: absolute; left: 56px; top: 36px;
    font-size: 15px; color: var(--label); letter-spacing: 0.5px;
  }
  .sign {
    position: absolute; left: 277px; top: 79px;
    width: 297px; height: 991px;
    background: linear-gradient(180deg, var(--sign-blue) 0%, var(--sign-blue-deep) 100%);
    overflow: hidden;
  }
  .brand {
    position: absolute; top: 112px; left: 0; width: 100%;
    display: flex; justify-content: center; align-items: center; gap: 10px;
    color: var(--white); font-weight: 900; font-size: 26px; letter-spacing: 0.5px;
  }
  .brand-dot { width: 14px; height: 14px; border-radius: 50%; background: var(--white); }
  .deco-illustration {
    position: absolute; left: 30px; top: 600px; width: 250px; height: 380px;
    border-radius: 18px;
    background: linear-gradient(200deg, rgba(156,198,238,0.55) 0%, rgba(230,240,250,0.45) 55%, rgba(156,198,238,0.25) 100%);
  }
  .corp-type {
    position: absolute; left: 57px; top: 198px;
    width: 62px;
    display: grid; grid-template-columns: 1fr 1fr;
    color: var(--white); font-weight: 900; font-size: 29px; line-height: 1.25;
    text-align: center;
  }
  .company-name {
    position: absolute; left: 62px; top: 290px;
    writing-mode: vertical-rl;
    color: var(--white); font-weight: 900; font-size: 92px;
    line-height: 1; letter-spacing: 0;
  }
  .service {
    position: absolute; left: 184px; top: 198px;
    display: flex; flex-direction: column; gap: 9px;
  }
  .service-tag {
    writing-mode: vertical-rl;
    width: 62px;
    color: var(--white); font-weight: 900; font-size: 48px;
    line-height: 62px; text-align: center;
    padding: 4px 0;
  }
  .service-tag--wall { background: var(--orange); }
  .service-tag--paint { background: var(--green); }
  .service-tag--shop { background: var(--maroon); }
  .footer-band {
    position: absolute; left: 0; top: 1128px; width: 848px; height: 32px;
    background: var(--sign-blue);
  }
  .caption {
    position: absolute; left: 0; top: 1168px; width: 100%;
    text-align: center; font-size: 15px; font-weight: 700; color: var(--ink);
  }
</style>
</head>
<body>
  <p class="size-label">H3600×W900</p>

  <section class="sign">
    <div class="brand"><span class="brand-dot"></span><span>HOSHIORANT</span></div>
    <div class="deco-illustration" role="img" aria-label="壁を塗り上げるペイントローラーと上向きの矢印のイラスト"></div>
    <div class="corp-type"><span>株</span><span>式</span><span>会</span><span>社</span></div>
    <h1 class="company-name">ホシオラント</h1>
    <div class="service">
      <span class="service-tag service-tag--wall">外壁</span>
      <span class="service-tag service-tag--paint">塗装</span>
      <span class="service-tag service-tag--shop">専門店</span>
    </div>
  </section>

  <div class="footer-band"></div>
  <p class="caption">㈱ホシオラント様 看板デザイン案</p>
</body>
</html>
```